Brookvale Urgent Care Clinic
Business card and stationary
Brookvale Urgent Care Clinic - Health
Creative Brief
Professional
2847 Quarrow Blvd, Suite 316 Dallas, Texas 75214
wolcastry@mailbrisk.com
www.BrookvaleUC.com
I only want the company name, physicial address and web site on the front with a design. On back only black and white map.
Black and white map of location

```html
<!DOCTYPE html>
<html lang="en">
<head>
<meta charset="utf-8">
<title>Brookvale Urgent Care Clinic – Stationery</title>
<link href="https://fonts.googleapis.com/css2?family=Cinzel:wght@700&family=Open+Sans:wght@400;600&display=swap" rel="stylesheet">
<style>
:root{
  --bg-dark:#141414;
  --bg-mid:#262626;
  --paper:#ffffff;
  --brand-red:#b3261e;
  --band-red:#e0452f;
  --band-pale:#f6c2b3;
  --ink:#555555;
  --line:#d6d6d6;
  --map-light:#eeeeee;
  --map-mid:#c9c9c9;
}
*{margin:0;padding:0;box-sizing:border-box}
html,body{width:1200px;height:607px;overflow:hidden}
body{background:radial-gradient(ellipse at center,var(--bg-mid),var(--bg-dark));position:relative;font-family:"Open Sans",sans-serif;color:var(--ink)}
.sheet{position:absolute;background:var(--paper);box-shadow:0 3px 10px rgba(0,0,0,.6);overflow:hidden}
.brand{display:flex;align-items:center;gap:6px;font-family:"Cinzel",serif;font-weight:700;color:var(--brand-red);line-height:1.05}
.brand-mark{border-radius:50%;background:var(--brand-red);flex:none}
.band{position:absolute;left:0;right:0;bottom:0;background:linear-gradient(to top,var(--band-red),var(--band-pale) 70%,rgba(255,255,255,0))}
.band .web{position:absolute;right:10px;bottom:5px;color:#fff;font-size:7px;font-weight:600}
.contact{position:absolute;text-align:right;font-size:5.5px;line-height:1.5}

.letterhead{top:72px;width:321px;height:509px}
.letterhead .brand{position:absolute;left:14px;top:16px;font-size:12px}
.letterhead .brand-mark{width:26px;height:26px}
.letterhead .contact{right:14px;top:18px}
.letterhead .band{height:48px}
.letterhead .faint{position:absolute;left:22px;bottom:34px;width:96px;height:96px;border-radius:50%;border:2px solid rgba(179,38,30,.07);background:rgba(179,38,30,.03)}
.lh-1{left:41px}.lh-2{left:389px}

.env{left:739px;width:432px}
.env-flap{top:36px;height:150px}
.env-flap .flap-fill{position:absolute;inset:0}
.env-flap .seal{position:absolute;left:50%;top:70px;width:26px;height:26px;margin-left:-13px;border-radius:50%;background:var(--brand-red);border:3px solid #fff}
.env-back{top:110px;height:150px}
.env-back svg{position:absolute;inset:0}
.env-back .seal{position:absolute;left:50%;top:44px;width:20px;height:20px;margin-left:-10px;border-radius:50%;background:var(--brand-red)}
.env-front{top:204px;height:144px}
.env-front .brand{position:absolute;left:12px;top:20px;font-size:10px}
.env-front .brand-mark{width:20px;height:20px}
.env-front .return{position:absolute;left:14px;top:58px;font-size:5.5px}
.env-front .band{height:34px}

.card{width:138px;height:76px}
.r1{top:396px}.r2{top:480px}
.c1{left:739px}.c2{left:886px}.c3{left:1033px}
.card-front .brand{position:absolute;left:0;right:0;top:12px;justify-content:center;font-size:7px;text-align:center}
.card-front .brand-mark{width:10px;height:10px}
.card-front .addr{position:absolute;left:0;right:0;top:38px;text-align:center;font-size:5px}
.card-front .band{height:18px}
.card-front .band .web{font-size:5px;bottom:3px;right:6px}
.map{position:absolute;inset:0;background:linear-gradient(135deg,var(--map-light),var(--map-mid) 50%,var(--map-light))}
.map-pin{position:absolute;right:14px;top:8px;width:8px;height:8px;border-radius:50%;background:var(--brand-red)}
</style>
</head>
<body>

<section class="sheet letterhead lh-1">
  <div class="brand"><span class="brand-mark"></span><span>BROOKVALE URGENT<br>CARE CLINIC</span></div>
  <div class="contact">2847 Quarrow Blvd, Suite 316<br>Dallas, Texas 75214<br>Tel (214) 555-0193<br>wolcastry@mailbrisk.com</div>
  <div class="faint"></div>
  <div class="band"><span class="web">www.BrookvaleUC.com</span></div>
</section>

<section class="sheet letterhead lh-2">
  <div class="brand"><span class="brand-mark"></span><span>BROOKVALE URGENT<br>CARE CLINIC</span></div>
  <div class="contact">2847 Quarrow Blvd, Suite 316<br>Dallas, Texas 75214<br>Tel (214) 555-0193<br>wolcastry@mailbrisk.com</div>
  <div class="faint"></div>
  <div class="band"><span class="web">www.BrookvaleUC.com</span></div>
</section>

<section class="sheet env env-flap">
  <svg class="flap-fill" viewBox="0 0 432 150" preserveAspectRatio="none">
    <defs><linearGradient id="flapRed" x1="0" y1="0" x2="0" y2="1">
      <stop offset="0" stop-color="#e0452f"/><stop offset="1" stop-color="#fbe1d9"/></linearGradient></defs>
    <path d="M0 0H432V30L216 96L0 30Z" fill="url(#flapRed)"/>
  </svg>
  <div class="seal"></div>
</section>

<section class="sheet env env-back">
  <svg viewBox="0 0 432 150" preserveAspectRatio="none">
    <path d="M0 0L216 70L432 0M0 150L180 60M432 150L252 60" fill="none" stroke="#cfcfcf" stroke-width="1"/>
  </svg>
  <div class="seal"></div>
</section>

<section class="sheet env env-front">
  <div class="brand"><span class="brand-mark"></span><span>BROOKVALE URGENT<br>CARE CLINIC</span></div>
  <div class="return">2847 Quarrow Blvd, Suite 316 Dallas, Texas 75214</div>
  <div class="band"><span class="web">www.BrookvaleUC.com</span></div>
</section>

<section class="sheet card card-front r1 c1">
  <div class="brand"><span class="brand-mark"></span><span>BROOKVALE URGENT<br>CARE CLINIC</span></div>
  <div class="addr">2847 Quarrow Blvd, Suite 316<br>Dallas, Texas 75214</div>
  <div class="band"><span class="web">www.BrookvaleUC.com</span></div>
</section>
<section class="sheet card r1 c2"><div class="map" role="img" aria-label="Black and white street map of the clinic location"></div><span class="map-pin"></span></section>
<section class="sheet card r1 c3"><div class="map" role="img" aria-label="Black and white street map of the clinic location"></div><span class="map-pin"></span></section>
<section class="sheet card r2 c1"><div class="map" role="img" aria-label="Black and white street map of the clinic location"></div><span class="map-pin"></span></section>
<section class="sheet card r2 c2"><div class="map" role="img" aria-label="Black and white street map of the clinic location"></div><span class="map-pin"></span></section>
<section class="sheet card r2 c3"><div class="map" role="img" aria-label="Black and white street map of the clinic location"></div><span class="map-pin"></span></section>

</body>
</html>
```